Online ticketing company needs new biz card design

Needing an updated business card to reflect our company, incorporating our existing logo and colour scheme (red, black, white). The design should communicate our modern, online, technology, innovation based company.

Details for card need to include the following:

Name
Position
Telephone and extension number
Mobile number
Email
Web address
Physical and/or postal address

Industry/Entity Type

Business

Font styles to use
Sans Serif

Requirements
Must have
• Clear, bold, eye catching design

```html
<!DOCTYPE html>
<html lang="en">
<head>
<meta charset="utf-8">
<title>TIXORA Business Card</title>
<link rel="stylesheet" href="https://fonts.googleapis.com/css2?family=Arimo:wght@400;700&family=Archivo+Black&family=Libre+Baskerville:ital@1&display=swap">
<style>
  :root {
    --ink: #050505;
    --red: #e3181f;
    --red-dark: #9e0f14;
    --white: #ffffff;
    --paper: #ffffff;
    --shadow: rgba(0, 0, 0, 0.45);
  }
  * { margin: 0; padding: 0; box-sizing: border-box; }
  html, body {
    width: 978px;
    height: 1200px;
    overflow: hidden;
    background: var(--paper);
  }
  .sheet {
    position: relative;
    width: 978px;
    height: 1200px;
  }
  .card {
    position: absolute;
    left: 21px;
    width: 938px;
    height: 569px;
    background: var(--ink);
    box-shadow: 2px 3px 8px var(--shadow);
    overflow: hidden;
  }
  .card--front { top: 14px; }
  .card--back { top: 612px; }
  .card-art {
    position: absolute;
    inset: 0;
    width: 938px;
    height: 569px;
  }
  .wordmark {
    position: absolute;
    font-family: "Archivo Black", "Arimo", sans-serif;
    color: var(--white);
    letter-spacing: 1px;
    transform: translate(-50%, -50%);
    white-space: nowrap;
    line-height: 1;
  }
  .card--front .wordmark { left: 233px; top: 324px; font-size: 62px; }
  .card--back .wordmark { left: 236px; top: 263px; font-size: 84px; }
  .holder {
    position: absolute;
    left: 478px;
    top: 176px;
    color: var(--white);
  }
  .holder-name {
    font-family: "Libre Baskerville", serif;
    font-style: italic;
    font-size: 29px;
    line-height: 1.1;
  }
  .holder-position {
    font-family: "Arimo", sans-serif;
    font-size: 19px;
    margin-top: 2px;
  }
  .contact {
    position: absolute;
    right: 112px;
    color: var(--white);
    font-family: "Arimo", sans-serif;
    font-size: 20px;
    text-align: right;
    line-height: 1.45;
    transform: translateY(-50%);
  }
  .contact--phone { top: 329px; }
  .contact--mobile { top: 387px; }
  .contact--email { top: 446px; }
  .contact--address { top: 516px; }
  .web-address {
    position: absolute;
    right: 19px;
    top: 342px;
    color: var(--red);
    font-family: "Arimo", sans-serif;
    font-weight: 700;
    font-size: 20px;
    letter-spacing: 2.6px;
  }
</style>
</head>
<body>
<main class="sheet">

  <section class="card card--front" aria-label="Business card front">
    <svg class="card-art" viewBox="0 0 938 569" aria-hidden="true">
      <defs>
        <clipPath id="front-arc-clip"><rect x="0" y="0" width="490" height="150"/></clipPath>
      </defs>
      <g class="accent-arc" clip-path="url(#front-arc-clip)">
        <circle cx="233" cy="319" r="340" fill="none" stroke="var(--red-dark)" stroke-width="24"/>
        <circle cx="233" cy="319" r="343" fill="none" stroke="var(--red)" stroke-width="18"/>
      </g>
      <g class="contact-strip">
        <rect x="888" y="0" width="50" height="569" fill="var(--red)"/>
        <line x1="888" y1="0" x2="888" y2="569" stroke="var(--white)" stroke-width="2"/>
        <g class="contact-badges" fill="var(--red)" stroke="var(--white)" stroke-width="2.5">
          <circle cx="888" cy="329" r="17"/>
          <circle cx="888" cy="387" r="17"/>
          <circle cx="888" cy="446" r="17"/>
          <circle cx="888" cy="516" r="17"/>
        </g>
        <rect x="889" y="300" width="16" height="240" fill="var(--red)"/>
      </g>
      <g class="contact-icons" fill="var(--white)">
        <path d="M883 321c1-1 2-1 3 0l2 3c0 1 0 2-1 2l-1 1c1 2 3 4 5 5l1-1c1-1 2-1 2 0l3 2c1 1 1 2 0 3l-2 2c-5 0-12-7-12-12z"/>
        <rect x="883" y="377" width="11" height="20" rx="2"/>
        <rect x="885" y="380" width="7" height="12" fill="var(--red)"/>
        <rect x="881" y="440" width="16" height="12" rx="1"/>
        <path d="M882 441l7 6 7-6" fill="none" stroke="var(--red)" stroke-width="1.6"/>
        <path d="M889 505a7 7 0 0 1 7 7c0 5-7 13-7 13s-7-8-7-13a7 7 0 0 1 7-7z"/>
        <circle cx="889" cy="512" r="2.6" fill="var(--red)"/>
      </g>
    </svg>

    <div class="wordmark">TIXORA</div>

    <div class="holder">
      <p class="holder-name">Name Last Name</p>
      <p class="holder-position">Position</p>
    </div>

    <p class="contact contact--phone">111-111-1111 ext.111</p>
    <p class="contact contact--mobile">222-222-2222</p>
    <p class="contact contact--email">name@ticketwavehub.com</p>
    <p class="contact contact--address">Physical and<br>postal address</p>
  </section>

  <section class="card card--back" aria-label="Business card back">
    <svg class="card-art" viewBox="0 0 938 569" aria-hidden="true">
      <defs>
        <clipPath id="back-arc-clip"><rect x="0" y="400" width="500" height="169"/></clipPath>
      </defs>
      <g class="accent-arc" clip-path="url(#back-arc-clip)">
        <circle cx="236" cy="250" r="335" fill="none" stroke="var(--red-dark)" stroke-width="24"/>
        <circle cx="236" cy="250" r="338" fill="none" stroke="var(--red)" stroke-width="18"/>
      </g>
    </svg>

    <div class="wordmark">TIXORA</div>

    <p class="web-address">www.ticketwavehub.com</p>
  </section>

</main>
</body>
</html>
```